You can visit www.tidecrestvitara.com
for your reference.
What we do :
Not just a nutrition plan, not just workout plan
Its a way of life
Balance between eating the right ingredients for your body, knowing what to avoid, taking care of the body (from skin care to muscle care (heart, lungs, organs...) to mental care)

Target Market(s)

Male and Female

Industry/Entity Type

Health And Wellness

Font styles to use
Script

Colors

Designer to choose colors to be used in the design.

Requirements
Must have
• Must focus of Longevity
Nice to have
• Include picture of Yasmeen in her description.
• You should get inspired from the concept of who we are and what we do for them to reflect this visually in the flyer
• What we do :
• Not just a nutrition plan, not just workout plan
• Its a way of life
• Balance between eating the right ingredients for your body, knowing what to avoid, taking care of the body (from skin care to muscle care (heart, lungs, organs...) to mental care)
Should not have
• Don't include the name Tidecrest Vitara and the Logo as well as the website just put VITARA. kindly use the pictures on the website and the girl doesn’t need to be blonde pick more Brunette, Arabic since we are promoting Dubai. Thank you

```html
<!DOCTYPE html>
<html lang="en">
<head>
<meta charset="utf-8">
<title>VITARA – The Science of Longevity</title>
<link href="https://fonts.googleapis.com/css2?family=Dosis:wght@200;300;400&family=Dancing+Script:wght@400&display=swap" rel="stylesheet">
<style>
:root{
  --teal:#0aa98a;
  --teal-text:#1a9c8a;
  --deep-blue:#106c98;
  --sky:#55b6e0;
  --sky-text:#45aedb;
  --pale-sky:#ddf1fa;
  --mist:#ecf7f5;
  --ink:#333;
  --white:#fff;
}
*{margin:0;padding:0;box-sizing:border-box}
html,body{width:848px;height:1200px;overflow:hidden;background:var(--white)}
.flyer{position:relative;width:848px;height:1200px;overflow:hidden;font-family:"Dosis",sans-serif;font-weight:300;color:var(--ink)}
.abs{position:absolute}
.shapes{position:absolute;left:0;top:0}
.photo-lead{left:0;top:0;width:277px;height:430px;background:linear-gradient(180deg,#f3ddd0 0%,#eccab8 35%,#d9735a 58%,#5f8f3a 75%,#3f6b2c 100%)}
.photo-kitchen{left:277px;top:0;width:277px;height:315px;background:linear-gradient(160deg,#d8d6d3 0%,#bdbab6 40%,#8d8985 65%,#e9e7e4 100%)}
.photo-portrait{left:582px;top:597px;width:236px;height:236px;border-radius:50%;background:radial-gradient(circle at 55% 45%,#f2e3e0 0%,#d9c4bf 35%,#8fa389 75%,#6f8a6e 100%)}
.wordmark{left:49px;top:296px;width:200px;text-align:center;color:var(--white);font-weight:200;font-size:48px;letter-spacing:1px;line-height:60px}
.questions{left:296px;top:348px;width:262px;color:var(--white);font-size:16.5px;line-height:21.5px}
.col-right{left:572px;width:270px}
.heading{color:var(--teal-text);font-size:17.5px;line-height:22px;text-align:center}
.benefits{list-style:none;font-size:16.5px;line-height:21.6px;color:var(--ink)}
.event{left:20px;top:514px;width:260px;text-align:center;color:var(--teal-text);font-size:21px;line-height:24px}
.tagline{left:290px;top:520px;width:265px;text-align:center;color:var(--teal-text);font-size:18px;line-height:21.5px}
.intro{left:11px;top:607px;width:254px;color:var(--white);font-size:11.4px;line-height:14.1px;text-align:justify}
.purpose{left:283px;top:595px;width:267px;height:177px;background:var(--pale-sky);color:var(--sky-text);font-size:17.5px;line-height:24px;text-align:center;padding-top:35px}
.services-title{left:20px;top:957px;width:240px;text-align:center;color:var(--teal-text);font-size:18px}
.services{left:15px;top:1014px;list-style:none;color:#555;font-size:13.5px;line-height:16.8px}
.testimonials-title{left:283px;top:796px;width:267px;text-align:center;color:var(--teal-text);font-size:18px}
.testimonials{left:283px;top:822px;width:266px}
.quote{font-family:"Dancing Script",cursive;font-size:14px;line-height:21px;text-align:justify;color:#333;margin-bottom:20px}
.bio{left:573px;top:846px;width:250px;font-size:11.2px;line-height:14px;text-align:justify;color:#555}
.bio p{margin-bottom:14px}
</style>
</head>
<body>
<main class="flyer">
  <div class="abs photo-lead" role="img" aria-label="Woman sipping through a straw from a bundle of fresh vegetables and fruit"></div>
  <div class="abs photo-kitchen" role="img" aria-label="Smiling brunette woman in workout wear sitting on a kitchen counter with healthy snacks"></div>

  <svg class="shapes" width="848" height="1200" viewBox="0 0 848 1200" aria-hidden="true">
    <circle cx="790" cy="70" r="120" fill="var(--mist)"/>
    <circle cx="600" cy="420" r="95" fill="var(--mist)" opacity=".7"/>
    <circle cx="820" cy="500" r="70" fill="var(--mist)" opacity=".8"/>
    <path d="M0,420 C60,345 150,315 277,315 L554,315 L554,510 L0,510 Z" fill="var(--teal)" opacity=".85"/>
    <path d="M0,445 C60,362 150,336 277,336 L554,336 L554,510 L0,510 Z" fill="var(--deep-blue)"/>
    <circle cx="149" cy="326" r="111" fill="var(--white)"/>
    <circle cx="149" cy="326" r="101" fill="var(--teal)"/>
    <path d="M0,590 H277 V880 C200,882 70,868 0,832 Z" fill="var(--sky)"/>
    <path d="M700,590 A125,125 0 0 1 700,840" fill="none" stroke="var(--pale-sky)" stroke-width="0"/>
    <path d="M640,598 A118,118 0 0 0 640,830" fill="none" stroke="#a9dcf0" stroke-width="14"/>
  </svg>

  <div class="abs photo-portrait" role="img" aria-label="Portrait of Yasmeen in a soft pink hood, hands pressed together outdoors"></div>

  <div class="abs wordmark">VITARA</div>

  <p class="abs questions">-Are you overwhelmed and exhausted and feel like there’s no time left for YOU?<br>-Are you struggling with Chronic Illness, Mood Swings, Bloating, and Hormone Imbalance?<br>-Have you gained weight due to stress-eating and ready take it off?</p>

  <h2 class="abs col-right heading" style="top:14px">Radiate Longevity and feel the best version of yourself!</h2>
  <ul class="abs col-right benefits" style="top:84px">
    <li>- &nbsp;Heal your gut</li>
    <li>- &nbsp;Balance your Hormone</li>
    <li>- &nbsp;Feel energetic</li>
    <li>- &nbsp;Look &amp; feel better than ever</li>
    <li>- &nbsp;Radiate and glow naturally</li>
    <li>- &nbsp;Improve nutrition through custom meal plans and counseling for pure vitality and longevity</li>
  </ul>
  <h2 class="abs col-right heading" style="top:270px">Functional Nutrition Education is one of the keys to a happier, healthier life.</h2>
  <ul class="abs col-right benefits" style="top:348px;left:578px">
    <li>- &nbsp;Personalized meal plans especially done according to your genes</li>
    <li>- &nbsp;Individualized health and wellness programs for pure vitality and longevity.</li>
    <li>- &nbsp;Achieve your longevity goals and have fun doing it.</li>
    <li>- &nbsp;Identify food sensitivities</li>
    <li>- &nbsp;Balance your hormone</li>
    <li>- Improve nutrition through meal plans</li>
    <li>- &nbsp;Counseling</li>
    <li>- Lose weight</li>
  </ul>

  <p class="abs event">The Science of Longevity<br>Dubai, November<br>8-10, 2019</p>
  <p class="abs tagline">TRANSFORM YOUR LIFESTYLE<br>BY<br>CHANGING THE WAY YOU LIVE</p>

  <p class="abs intro">-Yasmeen Saleh aboard certified, Transformational Wellness and Nutrition Expert, Member of the Institute of Integrative Health And of the Global Coaching Alliance (GCA) uses functional medicine, to help you find the answers to the root cause of disease instead of just treating symptoms. Individualized health and wellness programs for pure vitality and longevity. Pushing science and health forward.<br>Integrating whole person, mind, body and spirit towards healing and wellness. We educate our clients to be partners in their health care. Your health will be defined as more than the absence of disease, but as truth health and vitality where prevention is the best intervention.</p>

  <p class="abs purpose">Through this course, my purpose<br>is to inspire you and encourage you<br>to be the best version of yourself.<br>Performing up to your full potential<br>and access a greater level of your life.</p>

  <h3 class="abs services-title">Services Include:</h3>
  <ul class="abs services">
    <li>- &nbsp;WEIGHT LOSS COUNSELING</li>
    <li>- &nbsp;FUNCTIONAL NUTRITION EDUCATION</li>
    <li>- &nbsp;FOOD ALLERGY MANAGEMENT</li>
    <li>- &nbsp;GUT HEALTH</li>
    <li>- &nbsp;BALANCING HORMONE</li>
  </ul>

  <h3 class="abs testimonials-title">Testimonials</h3>
  <div class="abs testimonials">
    <p class="quote">I have more confidence! I struggled to lose weight and feel confident for years until I found the Renewal Reset Program which helped guide my lose 19.5 lbs! ” - Carla</p>
    <p class="quote">“My doctors told me that nutrition did not matter, I knew that was wrong. Now I feel amazing and hopeful again! I’ve reversed leaky Gut, ulcerative colitis, pain, fatigue, depression, and anxiety. ”-Brandon</p>
    <p class="quote">“After struggling with my health for many years, I finally found some answers to my health challenges. Going through the program, I lost 35 pounds, regained my confidence and rekindled my marriage.” - Delia</p>
  </div>

  <div class="abs bio">
    <p>Yasmeen Saleh is super passionate, board certified, Transformational Wellness and Nutrition Expert, Member of the Institute of Integrative Health And of the Global Coaching Alliance (GCA).</p>
    <p>Yasmeen a pharmaceutical graduate, realized that a systems biology approach was needed, similar to the views of traditional medicines, and thus shifted her focus to transformational functional wellness and nutrition with a focus on cross-cultural communication.</p>
    <p>On a quest to heal her own body and life, Yasmeen discovered that nutrition and health was much more than just food. To put together the pieces missing from her clinical nutrition training, she attended numerous universities, natural healing schools, seminars in every area of transformation. Today, Yasmeen works with a group of Doctors and Functional Medicine Practitioners, helping their patient to reach their health goals in areas such as achieving optimal weight, reducing food cravings, increasing sleep, and maximizing energy.</p>
  </div>
</main>
</body>
</html>
```